KRV Business Cards

We are a local commercial development company based in Silicon Valley and we would like a new business card. I've attached a copy of our company brochure to give a flavor of what we do, our logo, info company colors/graphics, and our current business card. We don't necessarily need a crazy makeover, but would like something that feels a little bit more "fresh" and modern (we've had the same business card design for 15+ years), but still in keeping with our overall brand -- clean, high-quality, modern but timeless. Would like to add our website to the info on the card (www.velmara.com) and would like the flexibility for some folks to have an efax number listed and some not to have that included (without it looking like there is a hole).

```html
<!DOCTYPE html>
<html lang="en">
<head>
<meta charset="utf-8">
<title>KRV Business Cards</title>
<link rel="stylesheet" href="https://fonts.googleapis.com/css2?family=Work+Sans:wght@400;500&display=swap">
<style>
  :root {
    --backdrop: #26282c;
    --brand-blue: #36526e;
    --card-white: #ffffff;
    --ink-light: #ffffff;
    --rule-light: rgba(255, 255, 255, 0.35);
  }
  * { margin: 0; padding: 0; box-sizing: border-box; }
  html, body {
    width: 1200px; height: 738px; overflow: hidden;
    background: var(--backdrop);
    font-family: "Work Sans", Arial, sans-serif;
  }
  .sheet {
    position: relative; width: 1200px; height: 738px;
    display: flex; align-items: center; justify-content: center; gap: 40px;
  }
  .card {
    position: relative; width: 520px; height: 297px; overflow: hidden;
  }

  /* Front */
  .card--front {
    background: var(--brand-blue);
    display: flex; align-items: center; justify-content: center;
  }
  .wordmark {
    color: var(--ink-light);
    font-weight: 400;
    text-transform: uppercase;
    letter-spacing: 0.06em;
    line-height: 1.12;
  }
  .card--front .wordmark { font-size: 27px; }

  /* Back */
  .card--back { background: var(--card-white); }
  .logo-plate {
    position: absolute; left: 46px; top: 115px;
    width: 192px; height: 101px;
    background: var(--brand-blue);
    display: flex; align-items: center; justify-content: center;
  }
  .logo-plate::after {
    content: ""; position: absolute; inset: 5px;
    border: 1px solid var(--rule-light);
  }
  .logo-plate .wordmark { font-size: 15px; }

  .info-panel {
    position: absolute; top: 0; right: 0; bottom: 0; width: 290px;
    background: var(--brand-blue);
    color: var(--ink-light);
    padding: 58px 0 0 50px;
  }
  .info-panel .notch {
    position: absolute; left: -12px; top: 92px;
  }
  .person-name { font-size: 19px; font-weight: 500; }
  .person-title { font-size: 12px; margin: 3px 0 0 6px; letter-spacing: 0.03em; }
  .address { font-size: 12.5px; line-height: 1.45; margin: 14px 0 0 14px; letter-spacing: 0.05em; }
  .contacts { list-style: none; margin: 14px 0 0 28px; font-size: 12.5px; letter-spacing: 0.05em; }
  .contacts li { display: flex; align-items: center; gap: 8px; line-height: 1.4; }
  .contacts svg { width: 9px; height: 9px; flex: none; }
</style>
</head>
<body>
<main class="sheet">
  <section class="card card--front" aria-label="Card front">
    <p class="wordmark">KRV Development<br>Company, LLC</p>
  </section>

  <section class="card card--back" aria-label="Card back">
    <div class="logo-plate">
      <p class="wordmark">KRV Development<br>Company, LLC</p>
    </div>

    <div class="info-panel">
      <svg class="notch" width="13" height="26" viewBox="0 0 13 26" aria-hidden="true">
        <polygon points="13,0 0,13 13,26" fill="#36526e"/>
      </svg>
      <h1 class="person-name">Dana L. Whitford</h1>
      <p class="person-title">Partner</p>
      <p class="address">218 Larkin Avenue<br>Sunnyvale, CA 94086</p>
      <ul class="contacts">
        <li>
          <svg viewBox="0 0 10 10" aria-hidden="true"><path d="M2 0.5 L3.6 2.6 L2.8 3.6 Q4 6 6.4 7.2 L7.4 6.4 L9.5 8 L8.4 9.5 Q3 9 0.5 1.6 Z" fill="#fff"/></svg>
          408.555.0142
        </li>
        <li>
          <svg viewBox="0 0 10 10" aria-hidden="true"><rect x="2.5" y="0.5" width="5" height="3" fill="#fff"/><rect x="0.5" y="3.5" width="9" height="4" rx="1" fill="#fff"/><rect x="2.5" y="6.5" width="5" height="3" fill="#fff"/></svg>
          408.555.0187
        </li>
        <li>
          <svg viewBox="0 0 10 10" aria-hidden="true"><rect x="0.8" y="2" width="8.4" height="6" fill="none" stroke="#fff" stroke-width="1"/><path d="M0.8 2 L5 5.5 L9.2 2" fill="none" stroke="#fff" stroke-width="1"/></svg>
          info@velmara.com
        </li>
        <li>
          <svg viewBox="0 0 10 10" aria-hidden="true"><circle cx="5" cy="5" r="4.3" fill="none" stroke="#fff" stroke-width="1"/><ellipse cx="5" cy="5" rx="1.8" ry="4.3" fill="none" stroke="#fff" stroke-width="0.8"/><line x1="0.7" y1="5" x2="9.3" y2="5" stroke="#fff" stroke-width="0.8"/></svg>
          www.velmara.com
        </li>
      </ul>
    </div>
  </section>
</main>
</body>
</html>
```